Business Card Design for Birchmont Financial

Financial services (financial & retirement planning, investment advice, finance brokering & risk insurance advice)

```html
<!DOCTYPE html>
<html lang="en">
<head>
<meta charset="utf-8">
<title>Birchmont Financial – Business Card</title>
<link rel="stylesheet" href="https://fonts.googleapis.com/css2?family=Libre+Baskerville:wght@400;700&display=swap">
<style>
  :root {
    --backdrop: #a9a9a9;
    --backdrop-light: #bdbdbd;
    --card-white: #f4f4f2;
    --card-black: #262626;
    --brand-green: #7a9a1c;
    --ink: #222222;
    --paper-text: #ffffff;
  }
  * { box-sizing: border-box; margin: 0; padding: 0; }
  html, body {
    width: 1200px; height: 889px; overflow: hidden;
  }
  body {
    background: radial-gradient(ellipse at 50% 30%, var(--backdrop-light), var(--backdrop));
    font-family: "Libre Baskerville", Georgia, serif;
    position: relative;
  }
  .card {
    position: absolute;
    top: 295px;
    width: 520px;
    height: 300px;
    box-shadow: 0 6px 18px rgba(0,0,0,0.25);
  }
  .card-front { left: 80px; background: var(--card-white); z-index: 1; }
  .card-back { left: 600px; background: var(--card-black); }

  .contact {
    position: absolute;
    right: 290px;
    top: 78px;
    text-align: right;
    color: var(--ink);
  }
  .contact-name {
    font-size: 17px;
    font-weight: 700;
    letter-spacing: 0.5px;
  }
  .contact-title {
    font-size: 10px;
    letter-spacing: 0.8px;
    margin-top: 4px;
    text-transform: uppercase;
  }
  .contact-line {
    font-size: 11px;
    letter-spacing: 1.2px;
    margin-top: 4px;
  }

  .brand-band {
    position: absolute;
    left: 250px;
    top: 130px;
    width: 400px;
    height: 92px;
    background: var(--brand-green);
    display: flex;
    align-items: center;
    padding-left: 40px;
    z-index: 2;
  }
  .brand-band .brand-name {
    color: var(--paper-text);
    font-size: 24px;
    font-weight: 400;
    letter-spacing: 1px;
  }

  .back-brand {
    position: absolute;
    right: 44px;
    bottom: 58px;
    text-align: center;
    color: var(--brand-green);
    font-weight: 400;
  }
  .back-brand .brand-mark {
    display: block;
    width: 70px; height: 70px;
    border-radius: 50%;
    background: var(--brand-green);
    margin: 0 auto 18px;
  }
  .back-brand .brand-name { font-size: 28px; letter-spacing: 1px; }
  .back-brand .brand-sub { font-size: 12px; letter-spacing: 6px; margin-top: 4px; }
</style>
</head>
<body>
  <section class="card card-front">
    <div class="contact">
      <p class="contact-name">EVAN HALE</p>
      <p class="contact-title">Director</p>
      <p class="contact-line">evan.hale@birchmont.com</p>
      <p class="contact-line">555 0142 7731</p>
      <p class="contact-line">www.birchmont.com</p>
    </div>
    <div class="brand-band">
      <span class="brand-name">BIRCHMONT</span>
    </div>
  </section>

  <section class="card card-back">
    <div class="back-brand">
      <span class="brand-mark"></span>
      <p class="brand-name">BIRCHMONT</p>
      <p class="brand-sub">FINANCIAL</p>
    </div>
  </section>
</body>
</html>
```